Leaflet and introduction email. designer required

To redesign our existing leaflet to more resemble our website style. The leaflet is to be a two fold A4 leaflet / menu for perspective customers who want physical further info on our company.
Also to redesign our attached PDF document into a better design. It will be emailed as a HTML email brochure introducing our company, with design style and link to our website. Food images available in addition to what is on our website
Target Market(s)
schools, nurseries, hospitals, and offices. Also local London boroughs.
Industry/Entity Type
Catering
Font styles to use
Other font styles liked:
- Heiti SC Light or similiar
Requirements
Must have
- modern quality feel. established company.
- follow company and Logo colours primarily.
Nice to have
- see website for style and fonts. www.amberkettle.catering
Should not have
- childish fonts and clip-art. design traits of attached documents, they should look more similiar to website.

```html
<!DOCTYPE html>
<html lang="en">
<head>
<meta charset="utf-8">
<title>Amber Kettle Catering – Menu</title>
<link href="https://fonts.googleapis.com/css2?family=Barlow:wght@300;400&family=Noto+Serif:wght@400&display=swap" rel="stylesheet">
<style>
  :root {
    --ink: #2b2b2b;
    --body: #3a3a3a;
    --white: #ffffff;
    --brand-green: #7cc26a;
    --rule: #333333;
  }
  * { margin: 0; padding: 0; box-sizing: border-box; }
  html, body { width: 1200px; height: 848px; overflow: hidden; background: var(--white); }
  .leaflet { position: relative; width: 1200px; height: 848px; color: var(--ink); font-family: "Barlow", Arial, sans-serif; }

  .heading { font-family: "Noto Serif", Georgia, serif; font-weight: 400; font-size: 23px; line-height: 30px; color: var(--ink); }
  .copy { font-weight: 300; font-size: 13.6px; line-height: 19px; letter-spacing: 0.35px; color: var(--body); text-align: justify; hyphens: auto; }
  .copy p + p { margin-top: 19px; }

  .column { position: absolute; width: 340px; }
  .column--global { left: 30px; top: 36px; }
  .column--about { left: 430px; top: 36px; }
  .column .heading { margin-bottom: 16px; }

  .brand { position: absolute; left: 868px; top: 78px; width: 240px; text-align: center;
    font-family: "Barlow", Arial, sans-serif; font-weight: 400; font-size: 30px; line-height: 34px; color: var(--brand-green); }

  .title { position: absolute; left: 880px; top: 222px; width: 240px; text-align: center;
    font-family: "Noto Serif", Georgia, serif; font-weight: 400; font-size: 68px; line-height: 80px; color: var(--ink); }
  .double-rule { position: absolute; height: 7px; border-top: 1.5px solid var(--rule); border-bottom: 1.5px solid var(--rule); }
  .double-rule--title { left: 963px; top: 312px; width: 75px; }
  .double-rule--service { left: 560px; top: 726px; width: 75px; }

  .photo-band { position: absolute; left: 0; top: 358px; width: 1200px; height: 310px; overflow: hidden; }
  .photo { position: absolute; top: 0; height: 310px; }
  .photo--cake { left: 0; width: 397px; background: radial-gradient(ellipse at 45% 55%, #e9e4dc 0%, #c49a58 35%, #6b625a 75%, #4e4a46 100%); }
  .photo--pasta { left: 397px; width: 408px; background: radial-gradient(ellipse at 50% 55%, #f1efea 0%, #c7704a 35%, #6f6a64 75%, #55514c 100%); }
  .photo--pie { left: 805px; width: 395px; background: linear-gradient(160deg, #8a8781 0%, #c19a6a 55%, #9a6b3f 100%); }
  .photo-caption { position: absolute; font-family: "Noto Serif", Georgia, serif; font-weight: 400; font-size: 25px; line-height: 32px; color: var(--white); }
  .photo-caption--simply { left: 30px; top: 17px; }
  .photo-caption--hot { left: 833px; top: 17px; }
  .photo-caption--daily { right: 26px; top: 204px; text-align: right; }

  .column--values { left: 30px; top: 692px; width: 340px; }
  .service-title { position: absolute; left: 470px; top: 686px; width: 255px; text-align: center; }

  .contact-tel { font-family: "Barlow", Arial, sans-serif; font-weight: 400; color: var(--ink); letter-spacing: 0.5px; }
  .contact-web { font-weight: 400; color: var(--ink); letter-spacing: 0.4px; }
  .contact--centre { position: absolute; left: 470px; top: 754px; }
  .contact--centre .contact-tel { font-size: 28px; line-height: 32px; }
  .contact--centre .contact-web { font-size: 19px; margin-top: 2px; padding-left: 4px; }
  .contact--right { position: absolute; left: 877px; top: 726px; }
  .contact--right .contact-tel { font-size: 27px; line-height: 32px; }
  .contact--right .contact-web { font-size: 18px; margin-top: -2px; }
  .social { display: flex; align-items: center; gap: 10px; margin-top: 6px; font-size: 13px; color: var(--ink); }
  .social svg { display: block; }
</style>
</head>
<body>
<main class="leaflet">
  <section class="column column--global">
    <h2 class="heading">Global Menu</h2>
    <div class="copy">
      <p>By creating meals inspired by countries all over the world, our kids have to opportunity to discover flavours and variety for their young taste buds. Encouraging healthy eating is our core value habits that we promote daily. With us, your little ones will receive the nutrients they need to develop.</p>
      <p>Some of the many ways we maintain our healthy eating standards is shown by our cleaner greener code (all green vegetables, e.g. peas, broccoli, spinach, kale), which we try to provide as much as we can weekly to serve with our protein and carbs. We also use Fair-trade &amp; free-range products wherever possible such as eggs, bananas, fruits.</p>
    </div>
  </section>

  <section class="column column--about">
    <h2 class="heading">About Us</h2>
    <div class="copy">
      <p>A professional and affordable contract catering company, delivering “hot food” to your business daily.</p>
      <p>We pride ourselves on top quality meals and service, and won’t scrimp on quality.</p>
      <p>We serve children’s nurseries and businesses in and around the M25 London area. We are expanding all the time. Contact us a call to see how we can help your business.</p>
      <p>From nurseries to businesses, we offer hot lunches &amp; tea for adults and children.</p>
    </div>
  </section>

  <div class="brand">Amber Kettle Catering</div>

  <h1 class="title">Menu</h1>
  <div class="double-rule double-rule--title"></div>

  <section class="photo-band">
    <div class="photo photo--cake" role="img" aria-label="Photo of a lemon loaf cake in a wooden tray with lemon wedges on a white plate"></div>
    <div class="photo photo--pasta" role="img" aria-label="Photo of penne pasta in tomato sauce with garlic bread and salad leaves in a white dish"></div>
    <div class="photo photo--pie" role="img" aria-label="Photo of a pie in a white bowl with salad leaves and sliced tomatoes on a wooden board"></div>
    <p class="photo-caption photo-caption--simply">Simply<br>delicious.</p>
    <p class="photo-caption photo-caption--hot">Deliciously<br>scrumptious<br>hot food,</p>
    <p class="photo-caption photo-caption--daily">delivered to the<br>workplace daily.<br>Yummy.</p>
  </section>

  <section class="column column--values">
    <div class="copy">
      <p>We believe young children deserve to be amazed with tasty, healthy food and do appreciate a wow factor put on a plate.</p>
      <p>No matter what you’re age, food should be an experience to enjoy</p>
    </div>
  </section>

  <h2 class="heading service-title">At Your Service</h2>
  <div class="double-rule double-rule--service"></div>
  <div class="contact contact--centre">
    <div class="contact-tel">Tel: 0203 555 0198</div>
    <div class="contact-web">www.amberkettle.catering</div>
  </div>

  <div class="contact contact--right">
    <div class="contact-tel">Tel: 0203 555 0198</div>
    <div class="contact-web">www.amberkettle.catering</div>
    <div class="social">
      <svg width="90" height="12" viewBox="0 0 90 12" aria-hidden="true">
        <circle cx="5" cy="6" r="4" fill="#2b2b2b"/>
        <circle cx="30" cy="6" r="4" fill="#2b2b2b"/>
        <circle cx="55" cy="6" r="4" fill="#2b2b2b"/>
        <circle cx="82" cy="6" r="4" fill="#2b2b2b"/>
      </svg>
      <span>#theAmberKettlecatering</span>
    </div>
  </div>
</main>
</body>
</html>
```